Lena Corvell Business Card

I need a business card that reflects my current website: itslenacorvell.example and screenshot attached. If we keep the color scheme of the site and sample card below that would be ideal. The business card should include the information on the attached sample cards.

Industry/Entity Type

Business

```html
<!DOCTYPE html>
<html lang="en">
<head>
<meta charset="utf-8">
<title>Lena Corvell Business Card</title>
<link rel="stylesheet" href="https://fonts.googleapis.com/css2?family=Francois+One&display=swap">
<style>
  :root {
    --paper: #ffffff;
    --ink: #111111;
    --teal-deep: #48b09a;
    --teal-soft: #6bc1b1;
    --type-light: #ffffff;
    --type-shadow: rgba(0, 0, 0, 0.35);
  }
  html, body {
    margin: 0;
    padding: 0;
    width: 1200px;
    height: 685px;
    overflow: hidden;
    background: var(--paper);
  }
  .card {
    position: relative;
    width: 1200px;
    height: 685px;
    background: var(--paper);
    font-family: "Francois One", "Arial Narrow", sans-serif;
    color: var(--type-light);
  }
  .brand-mark {
    position: absolute;
    top: 120px;
    left: 0;
    width: 1200px;
    text-align: center;
    font-size: 64px;
    line-height: 1;
    color: var(--ink);
    margin: 0;
    font-weight: 400;
  }
  .rule, .band {
    position: absolute;
    left: 0;
    width: 1200px;
  }
  .rule-top { top: 345px; height: 7px; background: var(--teal-soft); }
  .band-identity { top: 359px; height: 143px; background: var(--teal-deep); }
  .band-contact { top: 509px; height: 146px; background: var(--teal-soft); }
  .rule-bottom { top: 662px; height: 23px; background: var(--teal-deep); }

  .name {
    position: absolute;
    left: 39px;
    top: 381px;
    margin: 0;
    font-size: 46px;
    font-weight: 400;
    line-height: 1;
    letter-spacing: 0.3px;
    text-shadow: 1px 1px 2px var(--type-shadow);
  }
  .roles {
    position: absolute;
    left: 39px;
    top: 443px;
    margin: 0;
    font-size: 24px;
    line-height: 1;
    text-shadow: 1px 1px 2px var(--type-shadow);
  }
  .contact-item {
    position: absolute;
    display: flex;
    align-items: center;
    font-size: 28px;
    line-height: 1;
    text-shadow: 1px 1px 2px var(--type-shadow);
  }
  .contact-item svg { flex: none; }
  .contact-email { left: 39px; top: 540px; gap: 22px; }
  .contact-phone { left: 39px; top: 593px; gap: 22px; }
  .contact-social { left: 603px; top: 543px; gap: 14px; font-size: 26px; }
  .contact-web { left: 603px; top: 586px; gap: 16px; font-size: 26px; }
  .social-dot {
    width: 24px;
    height: 24px;
    border-radius: 50%;
    background: var(--type-light);
    flex: none;
  }
</style>
</head>
<body>
  <div class="card">
    <p class="brand-mark">its Lena Corvell</p>

    <div class="rule rule-top"></div>
    <div class="band band-identity"></div>
    <div class="band band-contact"></div>
    <div class="rule rule-bottom"></div>

    <h1 class="name">LENA CORVELL</h1>
    <p class="roles">Brand Curator I Digital Storyteller I Social Entrpreneur</p>

    <div class="contact-item contact-email">
      <svg width="28" height="20" viewBox="0 0 28 20" aria-hidden="true">
        <rect x="1" y="1" width="26" height="18" fill="none" stroke="#ffffff" stroke-width="1.6"/>
        <path d="M1 1 L14 12 L27 1 M1 19 L11 10 M27 19 L17 10" fill="none" stroke="#ffffff" stroke-width="1.6"/>
      </svg>
      <span>me@lenacorvell.example</span>
    </div>

    <div class="contact-item contact-phone">
      <svg width="28" height="28" viewBox="0 0 28 28" aria-hidden="true">
        <path d="M6 24 C2 18 4 8 12 4 L15 8 C11 10 9 15 11 19 Z M16 3 L20 1 L23 6 L19 8 Z M8 26 L11 22 L15 25 L12 28 Z" fill="#ffffff"/>
      </svg>
      <span>555.010.4821</span>
    </div>

    <div class="contact-item contact-social">
      <span class="social-dot"></span>
      <span>@itslenacorvell</span>
    </div>

    <div class="contact-item contact-web">
      <svg width="26" height="26" viewBox="0 0 26 26" aria-hidden="true">
        <g fill="none" stroke="#ffffff" stroke-width="1.5">
          <circle cx="13" cy="13" r="11.5"/>
          <ellipse cx="13" cy="13" rx="5" ry="11.5"/>
          <line x1="13" y1="1.5" x2="13" y2="24.5"/>
          <line x1="1.5" y1="13" x2="24.5" y2="13"/>
          <path d="M3.5 7 H22.5 M3.5 19 H22.5"/>
        </g>
      </svg>
      <span>www.itslenacorvell.example</span>
    </div>
  </div>
</body>
</html>
```